MODERN + COOL Business Card Needed!

SUMMARY
This is for a 40+ year old family business that is transitioning to the 2nd generation and is in real need of a more modern facelift. Ive attached a company logo (I made quickly as an idea with my limited PSD skills) to start off with that you are welcome to change and draw ideas from. Ive also attached some screen shots of cards I like to give you an idea of my preferences.

WHAT WE DO
The company name is Kin Dart HK Ltd. But I prefer to just call it Kin Dart or Kin Dart with Hong Kong as kind of a sub heading on the business card. We own a factory as well as help our customers find factories to make their product. Product I mean, toys 99.9% of the time. Simple old school toys like board games, puzzles, wooden toys, baby/infant toys.

You can say we are a "sourcing" or "trading" or "consulting" company with a factory to help you do it. But since we deal with toys, i like to keep it modern and cool and fun, not serious like managing hedge funds.

WHAT WE ARE LOOKING FOR
A cool, unique looking business card that stands out. In terms of design, something modern and professional. I like darker colored cards and I like colors such as blue/green/dark gray, but am open to other colored themes. I Like bright lime green with gray, always though thats a nice combo. I prefer cards that are all colored and not so much white showing (I think). Ive attached a few screenshots of cards so take a look to get a feel of what I like.

We do alot of wooden stacking games in variety of colors too like Pulto, Roni, Torvanets (google these to check them out). So designs that sort of resemble stacking or building would be cool but totally not necessary.

In terms of the physical aspects of the card, Im looking for a card a bit different than the standard rectangular shape. Double sided. Little things like having corner(s) be round or different angle instead of square edge I always thought was nice. Its got to be mostly a normal card size, no folding or smaller cards that fit weird in your wallet. No vertical designs. Am open to VERY different/creative shapes (as long as it still fits in a wallet good like a normal buisness card.

Hi everyone!

Just wanted to write a message to everyone to let them know all submissions are being reviewed or have been reviewed.  If I have not responded with feedback, rest assure your submission was definitely looked at in detail but I either have just been too busy to respond (alot of submissions!), or its on my to be considered list.

I respect and really enjoy receiving everyones creativity and work so I dont want it to go unrecognized - thus this message!  Feel free to submit more ideas if you like until this project ends.  Sometimes some designs just dont click but sometimes they can so you never know!

Thanks again for everyones participation and great work!

~Dov Ruel

Target Market(s)

The cards are mainly handed to toy company sourcers and buyers. People I talk to ... say Quelvin for example... might want to make their next edition of Farthundle game with a reputable factory at a good cost so they can sell it to stores at a profit.

So these are the types of people I often try to talk and introduce myself and my company to.

Industry/Entity Type

Building

Colors
acd036
0392cd
00a88e
474747
606060

Requirements
Must have
• Just double sided, not plain rectangle corners, and just cool to look at and catches your eye!

Oh and the obvious business card stuff like place for name, address, number, email, etc.
Nice to have
• Think more modern and fun, not serious and old fashion (thats what we used to be!). Can use the logo I attached and you can definitely alter and change the logo or make a whole new one!

Oh and can definitely use a creative slogan if you like to think of one based on what I described in what we do.
Should not have
• Dont use fonts or text placement that might make "Kin Dart" look like "Kind Art"... We arent selling news papers!!

Please nothing related to education since we have the word Dart in the title, thats not our business at all.

Logo and design should not be too heavy on things related to toys, as though thats what we primarily focus on now, what we do may change over time.

```html
<!DOCTYPE html>
<html lang="en">
<head>
<meta charset="utf-8">
<title>Kin Dart Ltd – Business Card</title>
<link rel="stylesheet" href="https://fonts.googleapis.com/css2?family=Libre+Baskerville:wght@700&family=Tinos&family=Open+Sans&display=swap">
<style>
  :root {
    --lime: #acd036;
    --charcoal: #474747;
    --paper: #ffffff;
    --ink: #000000;
    --serif-display: "Libre Baskerville", Georgia, serif;
    --serif-text: "Tinos", "Times New Roman", serif;
    --sans: "Open Sans", Arial, sans-serif;
  }
  html, body {
    margin: 0;
    padding: 0;
    width: 1200px;
    height: 1200px;
    overflow: hidden;
    background: var(--paper);
  }
  .canvas {
    width: 1200px;
    height: 1200px;
    overflow: hidden;
    position: relative;
  }
  .sheet {
    position: absolute;
    left: 0;
    top: 0;
    width: 1284px;
    height: 1284px;
    transform: scale(0.93458);
    transform-origin: 0 0;
    box-sizing: border-box;
    border: 1px solid #555;
  }
  .card-art {
    position: absolute;
    left: 0;
    top: 0;
  }
  .label {
    position: absolute;
    margin: 0;
    font-family: var(--sans);
    color: var(--ink);
    line-height: 1;
  }
  .label--side { font-size: 46px; }
  .label--front { left: 70px; top: 326px; }
  .label--back { left: 78px; top: 942px; }
  .label--note { font-size: 23px; left: 351px; top: 24px; }

  .brand {
    position: absolute;
    margin: 0;
    font-family: var(--serif-display);
    font-weight: 700;
    line-height: 1;
    letter-spacing: -1px;
  }
  .brand--name { left: 572px; top: 310px; font-size: 58px; color: var(--charcoal); }
  .brand--region { left: 572px; top: 366px; font-size: 34px; color: var(--charcoal); letter-spacing: -0.5px; }
  .brand--mark { color: var(--paper); font-size: 44px; }
  .brand--mark-front { left: 318px; top: 336px; }
  .brand--mark-back { left: 748px; top: 934px; }

  .holder {
    position: absolute;
    left: 404px;
    transform: translateX(-50%);
    margin: 0;
    color: var(--paper);
    font-family: var(--serif-text);
    text-align: center;
    white-space: nowrap;
    line-height: 1;
  }
  .holder--name { top: 906px; font-size: 29px; }
  .holder--role { top: 935px; font-size: 17px; }

  .contact {
    position: absolute;
    left: 322px;
    top: 1120px;
    margin: 0;
    padding: 0;
    list-style: none;
    font-family: var(--serif-text);
    font-size: 15.5px;
    color: var(--charcoal);
  }
  .contact li { height: 27.5px; line-height: 1; }
</style>
</head>
<body>
<main class="canvas">
  <div class="sheet">
    <svg class="card-art" width="1284" height="1284" viewBox="0 0 1284 1284" aria-hidden="true">
      <defs>
        <clipPath id="front-shape"><rect x="220" y="106" width="844" height="504" rx="46"/></clipPath>
        <clipPath id="back-shape"><rect x="220" y="705" width="844" height="504" rx="46"/></clipPath>
      </defs>

      <line x1="385" y1="52" x2="385" y2="246" stroke="#000" stroke-width="2"/>
      <polygon points="375,244 395,244 385,257" fill="#000"/>

      <g class="card card--front" clip-path="url(#front-shape)">
        <rect x="220" y="106" width="844" height="504" fill="var(--lime)"/>
        <polygon points="345,612 1066,404 1066,612" fill="var(--charcoal)"/>
        <line x1="345" y1="612" x2="1066" y2="404" stroke="var(--paper)" stroke-width="5"/>
      </g>

      <g class="card card--back" clip-path="url(#back-shape)">
        <rect x="220" y="705" width="844" height="504" fill="var(--charcoal)"/>
        <polygon points="218,999 936,1211 218,1211" fill="var(--lime)"/>
        <line x1="218" y1="999" x2="936" y2="1211" stroke="var(--paper)" stroke-width="5"/>
      </g>

      <g class="notches" fill="var(--paper)">
        <rect x="196" y="160" width="60" height="72" rx="14"/>
        <rect x="196" y="270" width="60" height="72" rx="14"/>
        <rect x="196" y="376" width="60" height="72" rx="14"/>
        <rect x="196" y="484" width="60" height="72" rx="14"/>
        <rect x="1028" y="160" width="60" height="72" rx="14"/>
        <rect x="1028" y="270" width="60" height="72" rx="14"/>
        <rect x="1028" y="376" width="60" height="72" rx="14"/>
        <rect x="1028" y="484" width="60" height="72" rx="14"/>

        <rect x="196" y="760" width="60" height="72" rx="14"/>
        <rect x="196" y="869" width="60" height="72" rx="14"/>
        <rect x="196" y="976" width="60" height="72" rx="14"/>
        <rect x="196" y="1084" width="60" height="72" rx="14"/>
        <rect x="1028" y="760" width="60" height="72" rx="14"/>
        <rect x="1028" y="869" width="60" height="72" rx="14"/>
        <rect x="1028" y="976" width="60" height="72" rx="14"/>
        <rect x="1028" y="1084" width="60" height="72" rx="14"/>
      </g>
    </svg>

    <p class="label label--note">cutout</p>
    <p class="label label--side label--front">front</p>
    <p class="label label--side label--back">back</p>

    <p class="brand brand--mark brand--mark-front">kin dart</p>
    <h1 class="brand brand--name">kin dart ltd</h1>
    <p class="brand brand--region">hong kong</p>

    <p class="brand brand--mark brand--mark-back">kin dart</p>
    <h2 class="holder holder--name">Ravi Desh</h2>
    <p class="holder holder--role">Managing Director</p>
    <ul class="contact">
      <li>Mb: 09812345670</li>
      <li>Email: ravidesk@postmail.com</li>
      <li>www.kindartltd.com</li>
    </ul>
  </div>
</main>
</body>
</html>
```